New website for our Escape Room

We are wanting to create a new website for our website. We have 2 different locations that guests will choose their location on the home page. Then we have 5 different escape room experiences. We like clean and fresh but fun. Our logo is black white and red. We like a modern feel that is simple to navigate. I love movement on the page. You can see our current site at quillhornpuzzles.com
We like fresh and modern. It needs to include much of the same information as out current site but we won't like the look of our site.

Target Market(s)

amusement, escape rooms.

Industry/Entity Type

escape room

Number of Pages Required

4 page

Requirements
Must have
• info on all 4 escape rooms, option to choose between Pigeon Forge and Nashville locations.

```html
<!DOCTYPE html>
<html lang="en">
<head>
<meta charset="utf-8">
<title>Quillhorn Puzzles — Escape Rooms</title>
<link rel="stylesheet" href="https://fonts.googleapis.com/css2?family=Antonio:wght@300;400;700&family=Open+Sans:wght@400;600;700&display=swap">
<style>
:root{
  --ink:#1f1f1f;
  --dark:#232323;
  --paper:#f3f3f3;
  --red:#e8262b;
  --red-deep:#b51c20;
  --text:#555;
  --white:#fff;
  --line:#cfcfcf;
}
*{box-sizing:border-box;margin:0;padding:0}
html,body{width:1200px;height:4132px;overflow:hidden}
body{position:relative;background:var(--paper);font-family:"Open Sans",sans-serif;color:var(--text)}
.abs{position:absolute}
.display{font-family:"Antonio",sans-serif;font-weight:400;text-transform:uppercase;color:var(--ink);letter-spacing:-1px;line-height:1}
.display .accent{color:var(--red)}
.centered{left:0;width:1200px;text-align:center}

/* header */
.hero-bg{left:0;top:0;width:1200px;height:690px}
.brand{font-family:"Antonio",sans-serif;font-weight:400;color:var(--white);text-transform:uppercase;line-height:1}
.site-brand{left:64px;top:22px;font-size:30px}
.main-nav{left:346px;top:32px;display:flex;gap:32px;font-size:9.5px;font-weight:700;color:var(--white);text-transform:uppercase}
.btn{background:var(--red);color:var(--white);font-size:9.5px;font-weight:700;text-transform:uppercase;display:flex;align-items:center;justify-content:center;border-radius:3px;box-shadow:0 2px 0 var(--red-deep)}
.nav-cta{left:993px;top:24px;width:144px;height:29px}
.hero-title{top:140px;font-size:78px;color:var(--white)}
.location{width:300px;text-align:center}
.location .loc-name{font-family:"Antonio",sans-serif;font-weight:400;color:var(--white);font-size:40px;line-height:1;text-transform:uppercase}
.location .loc-city{font-size:12px;font-weight:700;letter-spacing:3px;color:var(--red);text-transform:uppercase;margin-top:12px}
.location p{color:#d8d8d8;font-size:14px;line-height:22.5px;margin-top:14px}
.location .btn{width:104px;height:38px;margin:22px auto 0}
.loc-divider{left:600px;top:280px;width:1px;height:225px;background:#444}

/* rooms */
.rooms-title{top:770px;font-size:78px}
.room-card{top:911px}

/* about */
.about-title{top:1358px;font-size:78px}
.about-text{left:320px;top:1460px;width:560px;text-align:center;font-size:14px;line-height:22.5px}
.private{left:133px;top:1599px;width:934px;height:188px;border-radius:14px;background:linear-gradient(#ee3133,#b51d21);text-align:center;box-shadow:0 6px 14px rgba(0,0,0,.18)}
.private h2{color:var(--white);font-size:56px;margin-top:30px}
.private p{color:#fde1e1;font-size:14px;line-height:22.5px;width:560px;margin:14px auto 0}

/* benefits */
.benefits-title{top:1862px;font-size:80px;line-height:85px}
.benefit-divider{left:600px;top:2072px;width:1px;height:658px;background:var(--line)}
.benefit{width:260px}
.benefit .icon{width:48px;height:48px;border-radius:6px;background:#f6d6d7;border:2px solid var(--red)}
.benefit h3{font-family:"Antonio",sans-serif;font-weight:300;font-size:22px;line-height:31px;text-transform:uppercase;color:var(--ink);margin-top:10px}
.benefit.left{text-align:right}
.benefit.left .icon{margin-left:auto}

/* audiences */
.who-title{top:2832px;font-size:78px}
.audience{width:385px}
.audience .icon{width:62px;height:62px;border-radius:6px;background:#f6d6d7;border:2px solid var(--red)}
.audience h3{font-family:"Antonio",sans-serif;font-weight:300;font-size:22px;text-transform:uppercase;color:var(--ink);margin-top:10px}
.audience .lead{font-size:10.5px;font-weight:700;color:#2a2a2a;line-height:16.8px;margin-top:14px}
.audience .body{font-size:10.5px;line-height:16.8px;margin-top:16px;color:#777}

/* footer */
.footer-bg{left:0;top:3620px;width:1200px;height:512px}
.footer-brand{left:0;width:1200px;top:3778px;text-align:center;font-size:90px}
.social{top:3901px;left:532px;display:flex;gap:14px}
.social span{display:block;width:36px;height:36px;border-radius:50%;background:var(--red)}
.foot-rule{left:224px;width:752px;height:1px;background:#3d3d3d}
.footer-nav{top:4008px;left:224px;width:752px;display:flex;justify-content:space-around;font-size:10.5px;font-weight:700;color:var(--white);text-transform:uppercase}
.footer-nav i{color:var(--red);font-style:normal;font-weight:400}
.copyright{top:4085px;font-size:10.5px;color:#bbb}
</style>
</head>
<body>

<!-- header -->
<svg class="abs hero-bg" viewBox="0 0 1200 690" aria-hidden="true">
  <defs>
    <radialGradient id="heroGlow" cx="50%" cy="25%" r="60%">
      <stop offset="0" stop-color="#333"/>
      <stop offset="1" stop-color="#1c1c1c"/>
    </radialGradient>
  </defs>
  <rect width="1200" height="690" fill="url(#heroGlow)"/>
  <polygon points="0,640 600,588 1200,640 1200,690 0,690" fill="#e8262b"/>
  <polygon points="0,674 600,592 1200,674 1200,690 0,690" fill="#f3f3f3"/>
</svg>

<div class="abs brand site-brand">Quillhorn</div>
<nav class="abs main-nav">
  <span>Home</span><span>About</span><span>Escape Rooms ▾</span><span>FAQ</span><span>Gallery</span><span>Gift Cards</span><span>Contact</span>
</nav>
<div class="abs btn nav-cta">Find Your Location</div>

<h1 class="abs display centered hero-title">Find the location <span class="accent">room for you</span></h1>

<div class="abs location" style="left:250px;top:290px">
  <div class="loc-name">Quillhorn Puzzles</div>
  <div class="loc-city">Nashville</div>
  <p>Wheelchair Accessible<br>Rooms at Nashville: Ward Nine</p>
  <div class="btn">Book Now</div>
</div>
<div class="abs loc-divider"></div>
<div class="abs location" style="left:650px;top:290px">
  <div class="loc-name">Quillhorn Puzzles</div>
  <div class="loc-city">Pigeon Forge</div>
  <p>Wheelchair Accessible Rooms at<br>Pigeon Forge: Speakeasy, Hollow<br>Cabin, Ward Nine</p>
  <div class="btn">Book Now</div>
</div>

<!-- rooms -->
<h2 class="abs display centered rooms-title">Find the right <span class="accent">room for you</span></h2>

<svg class="abs room-card" style="left:0;width:244px;height:386px" viewBox="0 0 244 386" role="img" aria-label="Hollow Cabin room artwork: dark pine forest with room title">
  <defs><linearGradient id="cabinG" x1="0" y1="0" x2="1" y2="1"><stop offset="0" stop-color="#2e2e2e"/><stop offset="1" stop-color="#151515"/></linearGradient></defs>
  <path d="M0 10 Q120 18 244 0 V386 Q120 370 0 380 Z" fill="url(#cabinG)"/>
</svg>
<svg class="abs room-card" style="left:261px;width:677px;height:386px" viewBox="0 0 677 386" role="img" aria-label="Ward Nine room artwork: old hospital building at night with room title">
  <defs><linearGradient id="wardG" x1="0" y1="0" x2="0" y2="1"><stop offset="0" stop-color="#3a3a3a"/><stop offset="1" stop-color="#121212"/></linearGradient></defs>
  <path d="M0 0 Q338 40 677 0 V386 Q338 350 0 386 Z" fill="url(#wardG)"/>
</svg>
<svg class="abs room-card" style="left:956px;width:244px;height:386px" viewBox="0 0 244 386" role="img" aria-label="The Rock room artwork: island prison under a stormy sky with room title">
  <defs><linearGradient id="rockG" x1="0" y1="0" x2="1" y2="1"><stop offset="0" stop-color="#3b3838"/><stop offset="1" stop-color="#1a1a1a"/></linearGradient></defs>
  <path d="M0 0 Q120 18 244 10 V380 Q120 370 0 386 Z" fill="url(#rockG)"/>
</svg>

<!-- about -->
<h2 class="abs display centered about-title">About <span class="accent">us</span></h2>
<p class="abs about-text">QUILLHORN PUZZLES is the heart pounding, code-cracking, mind-bending race against time experience that will require everyone in your group's collective intellect, ingenuity, and problem-solving skills to escape.</p>

<section class="abs private">
  <h2 class="display" style="color:var(--white)">Upgrade to a private experience</h2>
  <p>Multiple parties can book the same room. If you would like to book a private experience, please contact us by phone .</p>
</section>

<!-- benefits -->
<h2 class="abs display centered benefits-title">Discover <span class="accent">the benefits<br>of escape rooms!</span></h2>
<div class="abs benefit-divider"></div>

<div class="abs benefit left" style="left:292px;top:2218px"><div class="icon" role="img" aria-label="Icon: group sharing ideas"></div><h3>Challenge your<br>creative thinking and<br>problem-solving skills</h3></div>
<div class="abs benefit left" style="left:292px;top:2462px"><div class="icon" role="img" aria-label="Icon: thumbs up"></div><h3>Improve<br>your mood</h3></div>
<div class="abs benefit" style="left:653px;top:2096px"><div class="icon" role="img" aria-label="Icon: people talking"></div><h3>Improve<br>communication and<br>social skills</h3></div>
<div class="abs benefit" style="left:653px;top:2342px"><div class="icon" role="img" aria-label="Icon: head with brain"></div><h3>Enhance and<br>build your memory</h3></div>
<div class="abs benefit" style="left:653px;top:2579px"><div class="icon" role="img" aria-label="Icon: puzzle pieces"></div><h3>Increase your<br>attention to detail</h3></div>

<!-- audiences -->
<h2 class="abs display centered who-title">Quillhorn <span class="accent">who</span></h2>

<article class="abs audience" style="left:172px;top:2954px">
  <div class="icon" role="img" aria-label="Icon: joined hands"></div>
  <h3>Team Building</h3>
  <p class="lead">What better way to foster synergy and teamwork than to be locked in a room together? Quillhorn escape games offer a one-of-a-kind team-building experience for corporate organizations, athletic teams, church groups, and more!</p>
  <p class="body">Our escape rooms test many aspects of your team and can help you figure out who responds best under pressure and who has the capabilities and skillset to get things done when it matters most. These group activities give your team the chance to have fun and build their chemistry! By relying on each other's creativity, thinking outside the box, communicating, cooperating, and leading, your employees will leave united and invigorated — as long as they make it out!</p>
</article>

<article class="abs audience" style="left:661px;top:2954px">
  <div class="icon" role="img" aria-label="Icon: game controller"></div>
  <h3>Gamers</h3>
  <p class="lead">Have you been looking for a way to impress your friends with your amazing cryptogram skills? Looking to take your strategic skills to an adventurous activity outside of the screen?</p>
  <p class="body">Look no further than Quillhorn Puzzles' escape rooms! Our rooms are sure to challenge even the most experienced puzzle solvers. We challenge you to think outside the box and get creative in order to decipher codes, riddles, puzzles, and brain teasers.</p>
</article>

<article class="abs audience" style="left:661px;top:3276px">
  <div class="icon" role="img" aria-label="Icon: family group"></div>
  <h3>Friends and Family</h3>
  <p class="lead">Bring your family, friends, neighbors, or a stranger you just met, and join us for an action-packed 60 minutes that you won't forget!</p>
  <p class="body">When you need fun family activities or you and your friends are looking for an adventurous activity in Pigeon Forge or Nashville, come to Quillhorn Puzzles for the best and most challenging escape rooms in the region!</p>
</article>

<article class="abs audience" style="left:172px;top:3346px">
  <div class="icon" role="img" aria-label="Icon: map with pin"></div>
  <h3>Tourists and Visitors</h3>
  <p class="lead">Looking for an interactive experience for your entire group to enjoy together? Located only a short distance from downtown Pigeon Forge and Nashville.</p>
  <p class="body">Quillhorn Puzzles offers a fun and challenging experience that everyone will enjoy. Come share an hour of your time with us!</p>
</article>

<!-- footer -->
<svg class="abs footer-bg" viewBox="0 0 1200 512" aria-hidden="true">
  <rect width="1200" height="512" fill="#1f1f1f"/>
  <polygon points="0,0 1200,0 1200,30 600,85 0,30" fill="#e8262b"/>
  <polygon points="0,0 1200,0 1200,5 600,80 0,5" fill="#f3f3f3"/>
</svg>
<div class="abs brand footer-brand">Quillhorn</div>
<div class="abs social" aria-label="Social links"><span></span><span></span><span></span></div>
<div class="abs foot-rule" style="top:3973px"></div>
<nav class="abs footer-nav">
  <span>Home</span><i>|</i><span>FAQs</span><i>|</i><span>Blog</span><i>|</i><span>Gift Cards</span><i>|</i><span>Contact</span><i>|</i><span>Privacy Policy</span>
</nav>
<div class="abs foot-rule" style="top:4053px"></div>
<p class="abs centered copyright">©2019 Quillhorn Puzzles - Do not copy. All rights reserved.</p>

</body>
</html>
```